Jewelry Business card for general purpose. Elegant and simple

We are a jewelry group with 6 stores in Mexico and 30 years in business.

We need a BC that at leats includes the name, mail, phone number and physical location (street, municipality, and county; example "Paseo Olmeda 2140", "Avenida Sotillo", "Monterrey").
Optional: we are trying to reposition the brand with the association of life-events or moments and family. Such as: birth, marriage, graduation, birthdays. Christmast, mothers day and fathers day.

We are looking for something elegant but simple

Jewelry name: "Lunetti". Email: "lunettibrillo@correo-ejemplo.mx". Phone num "4172-3095".

Target Market(s)

General business card: from suppliers to clients. One segment outstand: couples gettineg married

Industry/Entity Type

Jewelry Store

Contact Information for Business Card

Loking for something simple but elegant.

Font styles to use
Decorative
Script

Requirements
Must have
• Must have name, address, and mail.
Nice to have
• It could have jewelry pictures/design. Maybe quotes. Or general words as background . currently we have a very simple card with one ring would like to see something different.
Should not have
• Include real people.

```html
<!DOCTYPE html>
<html lang="es">
<head>
<meta charset="utf-8">
<title>Lunetti — Tarjeta de presentación</title>
<link rel="stylesheet" href="https://fonts.googleapis.com/css2?family=Open+Sans:wght@400&display=swap">
<style>
  :root {
    --stage: #3b3238;
    --card-white: #ffffff;
    --card-black: #000000;
    --ink-dark: #2a2a2a;
    --ink-grey: #6b6b6b;
    --swoosh: #e4e4e6;
    --swoosh-soft: #f0f0f2;
    --rule-grey: #5a5a5a;
    --ring-silver-light: #f2f3f6;
    --ring-silver-mid: #b9bcc4;
    --ring-sapphire: #1b2a6b;
  }
  * { margin: 0; padding: 0; box-sizing: border-box; }
  html, body { width: 1200px; height: 1200px; overflow: hidden; }
  body {
    background: var(--stage);
    font-family: "Open Sans", Arial, sans-serif;
    position: relative;
  }
  .card {
    position: absolute;
    left: 210px;
    width: 779px;
    height: 440px;
    overflow: hidden;
    box-shadow: 0 6px 14px rgba(0,0,0,0.45);
  }
  .card--front { top: 133px; background: var(--card-white); }
  .card--back  { top: 629px; background: var(--card-black); }

  .swoosh { position: absolute; inset: 0; }

  .ring-photo {
    position: absolute;
    border-radius: 48% 48% 46% 46%;
  }
  .card--front .ring-photo {
    left: 468px; top: 16px; width: 299px; height: 243px;
    background: radial-gradient(ellipse at 40% 35%, var(--ring-silver-light) 0%, var(--ring-silver-mid) 55%, var(--ring-sapphire) 100%);
    opacity: 0.85;
  }
  .card--back .ring-photo {
    left: 390px; top: 167px; width: 160px; height: 136px;
    background: radial-gradient(ellipse at 40% 35%, var(--ring-silver-light) 0%, var(--ring-silver-mid) 55%, var(--ring-sapphire) 100%);
    opacity: 0.8;
  }

  .holder { position: absolute; left: 46px; top: 56px; }
  .holder__name { font-size: 28px; color: var(--ink-dark); line-height: 1.2; }
  .holder__role { font-size: 19px; color: var(--ink-grey); line-height: 1.3; }

  .brand-name {
    position: absolute;
    font-weight: 400;
    line-height: 1;
    letter-spacing: 1px;
  }
  .card--front .brand-name { left: 366px; top: 205px; font-size: 72px; color: var(--ink-dark); }
  .card--back  .brand-name { left: 178px; top: 222px; font-size: 72px; color: var(--card-white); }

  .contact { position: absolute; left: 42px; top: 349px; list-style: none; }
  .contact li {
    display: flex; align-items: center; gap: 10px;
    font-size: 19px; color: var(--ink-grey); line-height: 26px;
  }
  .contact svg { width: 18px; height: 16px; flex: none; fill: var(--ink-dark); }

  .address {
    position: absolute; right: 43px; top: 322px;
    text-align: right; font-style: normal;
    font-size: 19px; line-height: 26px; color: var(--ink-grey);
  }

  .rule { position: absolute; height: 3px; background: var(--rule-grey); }
  .rule--left  { left: 0; top: 310px; width: 514px; }
  .rule--right { left: 544px; top: 237px; right: 0; }
</style>
</head>
<body>

  <section class="card card--front" aria-label="Frente de la tarjeta">
    <svg class="swoosh" viewBox="0 0 779 440" preserveAspectRatio="none" aria-hidden="true">
      <path d="M0 170 C120 140 260 170 400 225 C520 275 640 320 779 330 L779 350 C640 345 520 300 400 255 C260 200 120 175 0 205 Z" fill="var(--swoosh)"/>
      <path d="M10 240 C160 200 300 225 430 265 C560 305 680 330 779 330" stroke="var(--swoosh)" stroke-width="3" fill="none"/>
      <path d="M0 245 C150 210 290 235 420 275" stroke="var(--swoosh-soft)" stroke-width="8" fill="none"/>
    </svg>

    <div class="ring-photo" role="img" aria-label="Fotografía de anillo de plata con diamante central y dos zafiros azules"></div>

    <div class="holder">
      <p class="holder__name">mira lunetti</p>
      <p class="holder__role">managing director</p>
    </div>

    <p class="brand-name">Lunetti</p>

    <ul class="contact">
      <li>
        <svg viewBox="0 0 18 14" aria-hidden="true"><path d="M0 0h18v14H0z M2 2v1l7 5 7-5V2L9 7z M2 5v7h14V5l-7 5z" fill-rule="evenodd"/></svg>
        lunettibrillo@correo-ejemplo.mx
      </li>
      <li>
        <svg viewBox="0 0 18 16" aria-hidden="true"><path d="M1 5c0-3 16-3 16 0v2h-4V5H5v2H1z M4 8h10l2 8H2z M9 10a2 2 0 1 0 0 4a2 2 0 0 0 0-4z" fill-rule="evenodd"/></svg>
        4172-3095
      </li>
    </ul>

    <address class="address">
      Paseo Olmeda 2140,<br>
      Avenida Sotillo,<br>
      Monterrey
    </address>
  </section>

  <section class="card card--back" aria-label="Reverso de la tarjeta">
    <div class="rule rule--right"></div>
    <div class="rule rule--left"></div>
    <div class="ring-photo" role="img" aria-label="Fotografía de anillo de plata con diamante central y dos zafiros azules"></div>
    <p class="brand-name">Lunetti</p>
  </section>

</body>
</html>
```